Letterhead for a German Distribution/Manufacturing Company

We need a professional Letterhead in a unique Design.
not to playful.
The Letterhead has to show show that we are a international company with headquater in Germany.
all details like adress, Vat Tax Number, Bank Accout, Eori, email, Company number has to be on the Letterhead.
for example use: VAT TAX DE5704168 Bank Account: Norrfeld Bank IBAN DE421705238ß310482 Swift: KOLV3154802 EORI 3041296587 Company Number: HRB 61508 Adress: VOLTRINA UG Amsel Strasse 7 Postal Code 04683 City Lindmark Country: Germany Email: info@voltrina-example.com
the design can be colored but doesnt have to be
Industry/Entity Type
Manufacturing and international distribution
Requirements
Must have
- show that we are a international company with headquater in Germany. our company infos and logo

```html
<!DOCTYPE html>
<html lang="en">
<head>
<meta charset="utf-8">
<title>VOLTRINA UG – Letterhead</title>
<link rel="stylesheet" href="https://fonts.googleapis.com/css2?family=Montserrat:wght@400&family=Roboto:wght@400&display=swap">
<style>
  :root {
    --backdrop: #e9e9ea;
    --paper: #ffffff;
    --ink: #1c1c1c;
    --rule: #3a3a3a;
    --signature-tone: #d9d9d9;
  }
  * { box-sizing: border-box; margin: 0; padding: 0; }
  html, body {
    width: 1200px; height: 874px; overflow: hidden;
    background: var(--backdrop);
  }
  .letterhead {
    position: absolute; left: 303px; top: 17px;
    width: 594px; height: 840px;
    background: var(--paper);
    box-shadow: 0 2px 10px rgba(0,0,0,0.08);
    font-family: "Roboto", Arial, sans-serif;
    color: var(--ink);
    padding: 70px 56px 0 62px;
  }
  .brand {
    display: flex; align-items: center; gap: 10px;
    font-family: "Montserrat", Arial, sans-serif;
    font-weight: 400; font-size: 30px; letter-spacing: 1px;
  }
  .brand-dot {
    width: 34px; height: 34px; border-radius: 50%;
    background: var(--ink);
  }
  .recipient {
    margin-top: 62px;
    font-size: 9.6px; line-height: 1.35;
  }
  .body-copy p {
    font-size: 9.6px; line-height: 1.5;
    margin-top: 16px; text-align: justify;
  }
  .recipient + .body-copy p:first-child { margin-top: 8px; }
  .closing {
    margin-top: 20px; font-size: 9.6px;
  }
  .signature {
    margin-top: 10px; width: 120px; height: 44px;
    background: var(--signature-tone); border-radius: 2px;
  }
  .company-footer {
    position: absolute; left: 62px; right: 56px; bottom: 48px;
    border-top: 1px solid var(--rule);
    border-bottom: 1px solid var(--rule);
    padding: 8px 0 9px;
    text-align: center;
    font-size: 9px; line-height: 1.65;
  }
  .company-footer .sep { padding: 0 3px; }
  .mail-icon { vertical-align: -1px; margin: 0 2px 0 8px; }
</style>
</head>
<body>
  <main class="letterhead">
    <header class="brand">
      <span class="brand-dot"></span>
      <span class="brand-name">VOLTRINA</span>
    </header>

    <section class="recipient">
      <div>Mr/s</div>
      <div>First Name and Last Name</div>
      <div>Company Name</div>
      <div>Address</div>
    </section>

    <section class="body-copy">
      <p>Lorem Ipsum is simply dummy text of the printing and typesetting industry. Lorem Ipsum has been the industry's standard dummy text ever since the 1500s, when an unknown printer took a galley of type and scrambled it to make a type specimen book. It has survived not only five centuries, but also the leap into electronic typesetting, remaining essentially unchanged. It was popularised in the 1960s with the release of Typeset sheets containing Lorem Ipsum passages.</p>
      <p>The standard chunk of Lorem Ipsum used since the 1500s is reproduced below for those interested. Sections 1.10.32 and 1.10.33 from "de Finibus Bonorum et Malorum" by Varennius are also reproduced in their exact original form, accompanied by English versions from the 1914 translation by J. Tolvern. Lorem ipsum dolor sit amet, consectetur adipiscing elit, sed do eiusmod tempor incididunt ut labore et dolore magna aliqua.</p>
      <p>It is a long established fact that a reader will be distracted by the readable content of a page when looking at its layout. The point of using Lorem Ipsum is that it has a more-or-less normal distribution of letters, as opposed to using 'Content here, content here', making it look like readable English. Many desktop publishing packages and web page editors now.</p>
    </section>

    <section class="closing">
      <div>Your Sincerely,</div>
      <div class="signature" role="img" aria-label="Handwritten signature"></div>
    </section>

    <footer class="company-footer">
      <div>VOLTRINA UG Amsel Strasse 7 Postal Code 04683 City Lindmark Country: Germany
        <svg class="mail-icon" width="9" height="7" viewBox="0 0 9 7" aria-hidden="true"><rect x="0.5" y="0.5" width="8" height="6" fill="none" stroke="currentColor"/><path d="M0.5 0.8 L4.5 4 L8.5 0.8" fill="none" stroke="currentColor"/></svg>info@voltrina-example.com</div>
      <div>VAT TAX DE5704168<span class="sep">|</span>Bank Account: Norrfeld Bank IBAN DE421705238ß310482</div>
      <div>Swift: KOLV3154802 EORI 3041296587<span class="sep">|</span>Company Number: HRB 61508</div>
    </footer>
  </main>
</body>
</html>
```